Home Page Redesign for Pet Website

Looking to redesign the home page of our WORDPRESS website which will be renamed The Critter Cover Handbook 2015.

Looking for clean design which communicates clarity.
Updates

This is for a Wordpress site.

Please note that the design MUST include the content which is shown in the table in the brief!

Hi Thanks for the designs so far. We have just updated the brief to provide more information and clarify a few issues. We have also now included a couple of layout suggestions. They are just suggestions but it should give you a better idea of what we are looking for. And we have just increased the budget for 1st place by £120. Please feel free to message me if you have any questions. Many thanks. Maud

Please note that the new brief is in a file dated 25 Jan!

Reason: We have extended the deadline so we can continue working with the designers who have submitted designs we like. If you have any new designs please submit them by the original deadline of 7.37pm this evening (GMT). We are planning to make our final decision by Friday this week.

Target Market(s)

UK pet owners. All ages but largest age group is 35-50.

Industry/Entity Type

Insurance

Requirements
Must have
• Three clear content groups - LEARN, RESEARCH, CAMPAIGN (see brief for more details).
Stock photos with dogs and cats
Use current colour scheme
Must work with existing inner pages.
Existing font.. but 1pt larger
See brief for more details
Should not have
• Logo
Content from Existing Page (except for footer content... and menu headings).

```html
<!DOCTYPE html>
<html lang="en">
<head>
<meta charset="utf-8">
<title>The Critter Cover Handbook 2015</title>
<link href="https://fonts.googleapis.com/css2?family=Ubuntu:wght@300;400;500;700&display=swap" rel="stylesheet">
<style>
:root{
  --nav-blue:#6a9fd3;
  --nav-blue-dark:#5a8fc4;
  --panel-blue:#6ea3d2;
  --accent-red:#e8462e;
  --link-red:#d9372a;
  --ink:#1d1d1d;
  --body-ink:#333;
  --rule:#dddddd;
  --footer-bg:#1e1e1e;
  --footer-rule:#6b6b6b;
  --chirper-blue:#1da6e8;
  --friendwall-blue:#3b5a98;
  --searchly-red:#dd4b39;
}
*{box-sizing:border-box;margin:0;padding:0}
html,body{width:686px;height:1200px;overflow:hidden;background:#fff}
body{position:relative;font-family:"Ubuntu",Arial,sans-serif;color:var(--ink)}
.abs{position:absolute}

.main-nav{left:0;top:0;width:686px;height:27px;background:var(--nav-blue);display:flex;padding-left:100px}
.main-nav a{color:#fff;font-size:9px;text-decoration:none;line-height:27px;padding:0 18px;border-right:1px solid rgba(255,255,255,.25)}
.main-nav a.active{background:var(--nav-blue-dark)}
.main-nav a:last-child{border-right:none}

.site-header{left:0;top:27px;width:686px;height:66px;background:#f6f6f6}
.brand{left:107px;top:16px;display:flex;align-items:center;gap:6px}
.brand-mark{width:14px;height:14px;background:var(--nav-blue)}
.brand-name{font-size:12px;font-weight:500;color:var(--ink);line-height:1.2;width:110px}
.search{left:396px;top:19px;width:183px;height:24px;border:1.5px solid #222;background:#fff;font-size:8px;padding:6px 8px}
.search svg{position:absolute;right:6px;top:6px}

.hero{left:0;top:93px;width:686px;height:277px;background:linear-gradient(135deg,#c9b08a 0%,#e9e1d4 40%,#f4f1ec 60%,#b48a55 100%)}
.hero-rule{left:107px;width:471px;height:2px;background:#fff}
.hero-kicker{left:107px;top:143px;width:471px;text-align:center;color:#fff;font-size:16px;font-weight:300}
.hero-kicker b{font-weight:500}
.hero-title{left:107px;top:183px;width:471px;text-align:center;color:#fff;font-size:29px;font-weight:700;letter-spacing:-.5px}
.btn-cta{left:290px;top:238px;width:105px;height:26px;background:var(--accent-red);color:#fff;font-size:10px;text-align:center;line-height:26px}
.slide-dot{left:328px;top:304px;width:28px;height:28px;border-radius:50%;background:#1a1a1a;color:#fff;font-size:8px;text-align:center;line-height:28px}
.hero-tag{left:563px;top:93px;width:16px;height:16px;background:#fff}

.feature{left:107px;width:330px;height:96px}
.feature-photo{position:absolute;left:0;top:0;width:136px;height:96px}
.feature h2{position:absolute;left:148px;top:3px;width:185px;font-size:17px;font-weight:400;line-height:1.15}
.feature p{position:absolute;left:149px;font-size:6.6px;line-height:1.25;color:var(--body-ink);font-family:Arial,sans-serif;width:180px}
.feature .more{position:absolute;left:149px;font-size:6.5px;color:var(--link-red);font-family:Arial,sans-serif}
.divider{left:107px;width:323px;height:1px;background:var(--rule)}

.ad{left:450px;top:417px;width:128px;height:107px;background:#fff}
.ad-photo{position:absolute;left:0;top:0;width:128px;height:90px;background:linear-gradient(135deg,#b01e22,#e2463c 60%,#7a1014)}
.ad-line{position:absolute;right:8px;color:#fff;font-family:Arial,sans-serif;text-align:right}
.ad-btn{position:absolute;right:8px;top:72px;background:#f0a52a;color:#5a2a00;font-size:5px;padding:2px 6px;font-family:Arial,sans-serif}
.ad-brand{position:absolute;left:5px;top:94px;font-size:8px;font-weight:700;color:#333}
.ad-url{position:absolute;right:5px;top:96px;font-size:4.5px;color:#555;font-family:Arial,sans-serif}

.panel{left:450px;width:128px;background:var(--panel-blue);color:#fff;padding:0 9px}
.panel h3{font-weight:300;font-size:14px;line-height:1.2}
.panel p{font-size:6.3px;line-height:1.3;font-family:Arial,sans-serif}
.panel-year{display:flex;align-items:center;gap:4px;font-size:9px;margin:4px 0 7px}
.panel-year i{flex:1;height:1px;background:#fff}

.site-footer{left:0;top:944px;width:686px;height:228px;background:var(--footer-bg)}
.footer-head{color:#fff;font-size:10px;font-weight:500}
.footer-rule{height:2px;background:var(--footer-rule)}
.footer-links{left:107px;width:72px;list-style:none}
.footer-links li{color:#fff;font-size:6px;font-family:Arial,sans-serif;border-bottom:1px solid #888;padding:3px 0 4px}
.footer-links li:last-child{border:none}
.widget{top:979px;height:162px;background:#fff;font-family:Arial,sans-serif}
.widget-bar{height:21px;color:#fff;font-size:8.5px;font-family:"Ubuntu",sans-serif;line-height:21px;padding-left:22px;position:relative}
.widget-bar i{position:absolute;left:8px;top:6px;width:9px;height:9px;background:#fff;opacity:.85}
.widget small{font-size:4.5px;color:#555;display:block}
.social-btn{left:492px;width:86px;height:20px;color:#fff;font-size:7px;line-height:20px;padding-left:26px}
.social-btn i{position:absolute;left:9px;top:6px;width:8px;height:8px;background:#fff}
.legal{left:492px;top:1091px;color:#fff;font-size:6px;font-family:Arial,sans-serif;line-height:1.9}
.copyright{left:0;top:1172px;width:686px;height:28px;background:var(--nav-blue);color:#fff;font-size:5.5px;font-family:Arial,sans-serif;text-align:center;line-height:28px}
</style>
</head>
<body>

<nav class="main-nav abs">
  <a href="#">Home</a><a href="#" class="active">Pet Insurance Reviews</a><a href="#">Providers A-Z</a><a href="#">Pet Insurance Policies ▾</a><a href="#">Surveys</a><a href="#">More ▾</a>
</nav>

<header class="site-header abs">
  <div class="brand abs"><span class="brand-mark"></span><span class="brand-name">The Critter Cover Handbook 2015</span></div>
  <div class="search abs">Search
    <svg width="11" height="11" viewBox="0 0 11 11"><circle cx="4.5" cy="4.5" r="3.3" fill="none" stroke="#222" stroke-width="1.2"/><line x1="7" y1="7" x2="10" y2="10" stroke="#222" stroke-width="1.2"/></svg>
  </div>
</header>

<section class="hero abs" role="img" aria-label="Photo of a puppy and a kitten resting together in a wicker basket"></section>
<div class="hero-tag abs"></div>
<div class="hero-rule abs" style="top:137px"></div>
<div class="hero-kicker abs">Independent unbiased Information for Fellow <b>Pet Owners</b></div>
<div class="hero-rule abs" style="top:170px"></div>
<h1 class="hero-title abs">LEARN ABOUT PET INSURANCE</h1>
<div class="btn-cta abs">Call to Action »</div>
<svg class="abs" style="left:314px;top:310px" width="56" height="16" viewBox="0 0 56 16"><polyline points="7,2 2,8 7,14" fill="none" stroke="#222" stroke-width="1.5"/><polyline points="49,2 54,8 49,14" fill="none" stroke="#222" stroke-width="1.5"/></svg>
<div class="slide-dot abs">1</div>

<article class="feature abs" style="top:422px">
  <div class="feature-photo" role="img" aria-label="Photo of a woman cuddling a ginger cat" style="background:linear-gradient(135deg,#8a5a3a,#d9a27a 50%,#6e4a2f)"></div>
  <h2>Learn About Pet Insurance</h2>
  <p style="top:47px">Lorem ipsum dolor sit amet, consectetur adipisicing sed do eiusmod tempor incididunt ut labore et dolore magna aliqua. Ut enim ad minim veniam, quis ullamco laboris nisi ut aliquip ommodo consequat.</p>
  <span class="more" style="top:85px">Call to Action »</span>
</article>
<div class="divider abs" style="top:534px"></div>

<article class="feature abs" style="top:546px">
  <div class="feature-photo" role="img" aria-label="Photo of a family sitting on a sofa with their dog" style="background:linear-gradient(135deg,#d8d2c4,#a89878 50%,#c86a4a)"></div>
  <h2>Research Insurance Policies</h2>
  <p style="top:47px">Lorem ipsum dolor sit amet, consectetur adipisicing sed do eiusmod tempor incididunt ut labore et dolore magna aliqua. Ut enim ad minim veniam, quis ullamco laboris nisi ut aliquip ommodo consequat.</p>
  <span class="more" style="top:85px">Call to Action »</span>
</article>
<div class="divider abs" style="top:657px"></div>

<article class="feature abs" style="top:670px">
  <div class="feature-photo" role="img" aria-label="Photo of a smiling older woman holding a small dog" style="background:linear-gradient(135deg,#e8e4dc,#c43a4a 55%,#7a2a30)"></div>
  <h2>Compaign for Eairer Pet Insurance</h2>
  <p style="top:47px">Lorem ipsum dolor sit amet, consectetur adipisicing sed do eiusmod tempor incididunt ut labore et dolore magna aliqua. Ut enim ad minim veniam, quis ullamco laboris nisi ut aliquip ommodo consequat.</p>
  <span class="more" style="top:85px">Call to Action »</span>
</article>
<div class="divider abs" style="top:781px"></div>

<article class="feature abs" style="top:794px">
  <div class="feature-photo" role="img" aria-label="Photo of a girl with her dog in a sunny meadow" style="background:linear-gradient(135deg,#c8b060,#9aa84a 50%,#5e7a2a)"></div>
  <h2>Popular Resources</h2>
  <p style="top:32px">Lorem ipsum dolor sit amet, consectetur adipisicing sed do eiusmod tempor incididunt ut labore et dolore magna aliqua. Ut enim ad minim veniam, quis ullamco laboris nisi ut aliquip ommodo consequat.</p>
  <span class="more" style="top:70px">Call to Action »</span>
</article>

<aside class="ad abs">
  <div class="ad-photo" role="img" aria-label="Advert photo of a red car"></div>
  <div class="ad-line" style="top:6px;font-size:5.5px;line-height:1.5">Premium Cars.<br>Affordable Prices.</div>
  <div class="ad-line" style="top:36px;font-size:12px;font-weight:700;line-height:1">USED<br>CARS</div>
  <div class="ad-btn">Find Cars</div>
  <div class="ad-brand">Motorvale</div>
  <div class="ad-url">www.motorvale.example</div>
</aside>

<section class="panel abs" style="top:534px;height:188px;padding-top:18px">
  <h3>Welcome to The Critter Cover Handbook</h3>
  <div class="panel-year"><i></i>2015<i></i></div>
  <p>Lorem ipsum dolor sit amet, consectetur adipisicing elit, sed do eiusmod tempor incididunt ut labore et dolore magna aliqua. Ut enim ad minim veniam, nostrud exercitation ullamco laboris nisi ut aliquip ex ea commodo consequat. Duis aute irure dolor reprehenderit in voluptate velit esse dolore eu fugiat nulla ollit anim</p>
</section>

<section class="panel abs" style="top:734px;height:156px;padding-top:18px">
  <h3 style="font-size:14.5px">Disclaimer</h3>
  <div style="height:1px;background:#fff;margin:5px 0 9px"></div>
  <p>Please note that pet insurance terms often change. Whilst we will do our best to keep this website up to date you must check with the appropriate insurer before making any decisions. If you find any mistakes on this website please do let us know so we can correct it for the benefit of future visitors. Many thanks!</p>
</section>

<footer class="site-footer abs"></footer>
<div class="footer-head abs" style="left:107px;top:985px">About Us</div>
<div class="footer-rule abs" style="left:107px;top:1003px;width:72px"></div>
<ul class="footer-links abs" style="top:1018px">
  <li>Home</li><li>Pet Insurance Reviews</li><li>Providers A-Z</li><li>Insurance Policies</li><li>Surveys</li><li>More</li>
</ul>

<div class="widget abs" style="left:209px;width:120px">
  <div class="widget-bar" style="background:var(--friendwall-blue)"><i></i>Join us on Friendwall</div>
  <div style="padding:10px 6px 0 30px;position:relative;font-size:5px;color:var(--friendwall-blue);font-weight:700">
    <span style="position:absolute;left:6px;top:9px;width:18px;height:18px;background:#c9a89a"></span>
    Critter Cover Surveys UK<small>Like · 1,176</small>
  </div>
  <div style="margin:6px 6px 0;border-top:1px solid #ddd;padding-top:4px;font-size:5px;color:var(--friendwall-blue);font-weight:700;padding-left:20px;position:relative">
    <span style="position:absolute;left:0;top:4px;width:14px;height:14px;background:#c9a89a"></span>
    Critter Cover Surveys UK<small>January 14 at 1:48pm</small>
  </div>
  <p style="font-size:5px;color:#333;padding:6px 6px 3px">A sad story about the realities of third party liability cover!</p>
  <div role="img" aria-label="Photo of a small grey terrier" style="margin:0 6px;height:44px;background:linear-gradient(135deg,#d8c8b4,#6a6a6a)"></div>
</div>

<div class="widget abs" style="left:341px;width:125px">
  <div class="widget-bar" style="background:var(--chirper-blue)"><i></i>Latest from Chirper</div>
  <div style="padding:6px 8px;font-size:5.5px;font-weight:700;border-bottom:1px solid #eee">Tweets</div>
  <div style="padding:4px 8px 0 22px;font-size:4.8px;position:relative;color:#333;line-height:1.35">
    <span style="position:absolute;left:8px;top:5px;width:10px;height:10px;background:#c9a89a"></span>
    <b>Critter Cover Surveys</b> <span style="float:right;color:#888">16 Jun</span><small>@CritterSurveys</small>
    RT <span style="color:var(--chirper-blue)">@helperhounds</span>: Not into football? We have 14 adorable hearing dog puppies who will change your mind <span style="color:var(--chirper-blue)">#WorldCup</span>
  </div>
  <div role="img" aria-label="Photo of a spaniel puppy on grass" style="margin:4px 8px 0 8px;height:34px;background:linear-gradient(135deg,#8aa85a,#e8e0d0 60%,#5e7a3a)"></div>
  <div style="position:absolute;left:8px;right:3px;bottom:8px;border:1px solid #ddd;font-size:4.8px;color:#777;padding:3px">Tweet to @CritterSurveys</div>
</div>

<div class="footer-head abs" style="left:491px;top:979px">Follow Us</div>
<div class="footer-rule abs" style="left:491px;top:1002px;width:87px"></div>
<div class="social-btn abs" style="top:1014px;background:var(--chirper-blue)"><i></i>Follow Chirper</div>
<div class="social-btn abs" style="top:1038px;background:var(--friendwall-blue)"><i></i>Friendwall Like</div>
<div class="social-btn abs" style="top:1062px;background:var(--searchly-red)"><i></i>Follow on Searchly</div>
<div class="legal abs">Legal Information &amp; Disclaimers<br>Privacy Policy</div>

<div class="copyright abs">Copyright © 2015. The Critter Cover Handbook 2015, UK. All Right Reserved</div>

</body>
</html>
```